Wedding Videography Wordpress Website Theme

We need a modern and high-end website look for our wedding video and film business. We film weddings all over the United Kingdom and at European destinations so need something to reflect our work. The website should be visually stunning with images and videos being the focal point as this is what our services are.

The current website is www.lorenbrisk.example so you will be able to see our brand.

My Instagram is www.instagram.com/lorenbriskfilms so a new design should link in with this idea.

We need the following pages designed by the winning designer

1 - Homepage
2 - Films Index Page
3 - Testimonials
4 - Prices
5 - Reviews
6 - Meet Loren (About)
7 - Contact
8 - Blog Index
9 - Blog Page

All pages must be consistent so have a similar style.

Pages on menu:
Meet Loren
Videos
Packages
Testimionials
Journal (Blog)
Contact

We require a responsive look too. Over 90% of our visitors access the website via their mobile devices.

```html
<!DOCTYPE html>
<html lang="en">
<head>
<meta charset="utf-8">
<title>Testimonials – Loren Brisk Wedding Films</title>
<link rel="stylesheet" href="https://fonts.googleapis.com/css2?family=Cormorant+Garamond:wght@500;600&family=Jost:wght@300;400;500&display=swap">
<style>
:root{
  --gold:#b39a5b;
  --gold-soft:#e6dcbf;
  --sand:#e4d6ae;
  --band:#e9dec0;
  --ink:#2f2f2f;
  --text:#555;
  --muted:#999;
  --white:#fff;
}
*{margin:0;padding:0;box-sizing:border-box}
html,body{width:1200px;height:5098px;overflow:hidden}
body{position:relative;background:var(--white);font-family:'Jost',sans-serif;color:var(--text)}
.abs{position:absolute}
.serif{font-family:'Cormorant Garamond',serif}

/* hero */
.hero{left:0;top:0;width:1200px;height:617px;background:linear-gradient(100deg,#1f2a1c 0%,#38472f 30%,#5a5a4c 55%,#2e352a 75%,#6a6c64 100%)}
.hero-shade{left:0;top:0;width:1200px;height:617px;background:linear-gradient(180deg,rgba(0,0,0,.35),rgba(0,0,0,.15) 40%,rgba(0,0,0,.45))}
.brand{text-align:center;color:var(--white);font-family:'Jost',sans-serif;font-weight:400}
.brand-name{font-size:17px;letter-spacing:4px}
.brand-sub{font-size:8px;letter-spacing:5px;margin-top:3px}
.brand-mark{width:22px;height:22px;border:1.5px solid currentColor;margin:0 auto 8px}
.nav a{position:absolute;top:81px;color:var(--white);font-size:11px;font-weight:500;letter-spacing:.4px;text-decoration:none;white-space:nowrap}
.nav a.active::after{content:"";position:absolute;left:0;right:0;top:22px;height:2px;width:16px;margin:0 auto;background:var(--white)}
.enquire{left:940px;top:64px;width:143px;height:44px;background:var(--sand);color:var(--ink);font-size:11px;font-weight:500;display:flex;align-items:center;justify-content:center}
.hero-title{left:0;width:1200px;top:294px;text-align:center;color:var(--gold);font-size:36px;letter-spacing:2px;font-weight:500}
.hero-sub{left:0;width:1200px;top:352px;text-align:center;color:#eee;font-size:15px}

/* intro */
.intro-title{left:0;width:1200px;top:658px;text-align:center;color:var(--gold);font-size:27px;font-weight:500;letter-spacing:1.5px}
.intro-text{left:230px;width:740px;top:720px;text-align:center;font-size:12.5px;line-height:26.5px;font-weight:300}

/* testimonials */
.photo{overflow:hidden}
.play{position:absolute;width:48px;height:48px}
.avatar{border-radius:50%;border:3px solid #d8c99c;background:linear-gradient(135deg,#c9b68f,#6f6455)}
.couple{font-size:17px;font-weight:600;color:var(--ink);letter-spacing:.8px;white-space:nowrap}
.venue{font-size:10px;color:#aaa;font-weight:300;white-space:nowrap}
.quote{font-size:12.5px;line-height:26.5px;font-weight:300;color:var(--text);text-align:center}
.quote-mark{font-family:'Cormorant Garamond',serif;font-size:170px;color:#f0ede6;line-height:1}
.num{font-size:26px;color:var(--gold-soft);font-weight:300}
.rule{height:1px;background:var(--gold-soft)}

.btn-more{left:494px;top:4214px;width:211px;height:43px;background:var(--sand);color:var(--ink);font-size:11px;font-weight:500;display:flex;align-items:center;justify-content:center}

/* instagram */
.insta{left:0;top:4322px;width:1200px;height:473px;background:var(--band)}
.insta-title{left:0;width:1200px;top:4388px;text-align:center;color:#7a7050;font-size:27px;letter-spacing:7px;font-weight:500}
.tile{top:4470px;width:145px;height:162px}
.follow{left:471px;top:4687px;width:257px;height:53px;background:var(--white);color:var(--ink);font-size:13px;display:flex;align-items:center;justify-content:center}

/* footer */
.foot-brand{color:var(--gold)}
.foot-head{font-size:15px;font-weight:500;color:var(--ink);display:flex;align-items:center;gap:8px}
.foot-head::after{content:"";width:20px;height:1px;background:#bbb}
.foot-link{font-size:12px;color:var(--text);font-weight:300;white-space:nowrap}
.social{top:4976px;width:24px;height:24px;border:1.5px solid var(--gold);border-radius:4px}
.copy{left:0;width:1200px;top:5057px;text-align:center;font-size:10px;color:#aaa;font-weight:300}
</style>
</head>
<body>

<!-- Hero -->
<div class="abs hero" role="img" aria-label="Couple embracing beside a misty waterfall and green cliffs"></div>
<div class="abs hero-shade"></div>
<div class="abs brand" style="left:112px;top:28px;width:196px">
  <div class="brand-mark"></div>
  <div class="brand-name">LOREN BRISK</div>
  <div class="brand-sub">WEDDING FILMS</div>
</div>
<nav class="nav">
  <a style="left:396px">MEET LOREN</a>
  <a style="left:511px">VIDEOS</a>
  <a style="left:600px">PACKAGES</a>
  <a class="active" style="left:709px">TESTIMONIALS</a>
  <a style="left:837px">JOURNAL</a>
</nav>
<div class="abs enquire">ENQUIRE</div>
<h1 class="abs hero-title serif">TESTIMONIALS</h1>
<div class="abs hero-sub">Reviews From Real Couples</div>

<!-- Intro -->
<h2 class="abs intro-title serif">WEDDING VIDEO REVIEWS</h2>
<p class="abs intro-text">I have been invited to some amazing weddings all over the North East, UK and Europe. My main aim is to ensure that couples enjoy their day and that they take in the moments so they remember them. Here are some amazing wedding video reviews from brides, grooms and couples who I've been lucky to share their big day with.</p>

<!-- 01 -->
<div class="abs photo" style="left:0;top:851px;width:660px;height:479px;background:linear-gradient(120deg,#1c2218,#3d4a33 45%,#b0aa94 75%,#5a6148)" role="img" aria-label="Groom and bride looking up together in soft evening light"></div>
<svg class="play" style="left:298px;top:1066px" viewBox="0 0 48 48"><circle cx="24" cy="24" r="22" fill="rgba(255,255,255,.75)"/><path d="M19 15l14 9-14 9z" fill="#555"/></svg>
<div class="abs avatar" style="left:738px;top:880px;width:78px;height:78px" role="img" aria-label="Couple portrait"></div>
<div class="abs couple serif" style="left:829px;top:893px">HELENA &amp; MARCUS</div>
<div class="abs venue" style="left:830px;top:921px">Ashby Grange, Yorkshire</div>
<div class="abs quote-mark" style="left:820px;top:945px">&ldquo;</div>
<p class="abs quote" style="left:712px;top:990px;width:355px">What can I say other than — INCREDIBLE!! We weren't going to get a videographer but are so glad we did. Loren has captured the whole day in the most beautiful way, with a magical video, we both can't stop watching it! If anyone is unsure about a videographer we would highly recommend getting one! We cannot recommend Loren and his team enough! They made us feel at ease and most of the time we didn't even realise they were there. We had our film back within 24hours of our wedding finishing!! Loren we cannot thank you enough for what you have created for us!! THANK YOU.</p>
<div class="abs num" style="left:818px;top:1310px">01</div>
<div class="abs rule" style="left:855px;top:1329px;width:345px"></div>

<!-- 02 -->
<div class="abs photo" style="left:542px;top:1433px;width:658px;height:479px;background:linear-gradient(180deg,#1a2fa0 0%,#5a3fb8 30%,#e0286a 55%,#3040a8 80%,#101a50)" role="img" aria-label="Silhouette of a couple against a vivid sunset sky"></div>
<svg class="play" style="left:854px;top:1656px" viewBox="0 0 48 48"><circle cx="24" cy="24" r="22" fill="rgba(255,255,255,.75)"/><path d="M19 15l14 9-14 9z" fill="#555"/></svg>
<div class="abs avatar" style="left:185px;top:1500px;width:78px;height:78px" role="img" aria-label="Couple portrait"></div>
<div class="abs couple serif" style="left:280px;top:1515px">SOPHIE + DECLAN</div>
<div class="abs venue" style="left:280px;top:1543px">Fernley Manor, Leicestershire</div>
<div class="abs quote-mark" style="left:262px;top:1566px">&ldquo;</div>
<p class="abs quote" style="left:140px;top:1610px;width:340px">"We want to say a huge thank you to Loren. The video he created was just amazing. Loren and Owen just moved around like you didn't know you they were there. You caught everything on the day perfectly and it was great having you around."</p>
<p class="abs quote" style="left:140px;top:1772px;width:340px;font-weight:400;color:#444">Married at Fernley Manor,<br>Leicestershire</p>
<div class="abs rule" style="left:0;top:1912px;width:345px"></div>
<div class="abs num" style="left:360px;top:1893px">02</div>

<!-- 03 -->
<div class="abs photo" style="left:0;top:2010px;width:1200px;height:520px;background:linear-gradient(180deg,#c8cfc6 0%,#7c8f6c 25%,#4e6a36 55%,#3d5a2a 100%)" role="img" aria-label="Groom carrying bride across a hillside garden with mountains behind"></div>
<svg class="play" style="left:576px;top:2236px" viewBox="0 0 48 48"><circle cx="24" cy="24" r="22" fill="rgba(255,255,255,.75)"/><path d="M19 15l14 9-14 9z" fill="#555"/></svg>
<div class="abs avatar" style="left:560px;top:2495px;width:80px;height:80px" role="img" aria-label="Couple portrait"></div>
<div class="abs couple serif" style="left:0;width:1200px;text-align:center;top:2592px">ROWAN AND ELLIOT</div>
<div class="abs venue" style="left:0;width:1200px;text-align:center;top:2620px">Hollins Barn, Northumberland</div>
<div class="abs quote-mark" style="left:540px;top:2640px">&ldquo;</div>
<div class="abs" style="left:155px;top:2688px;width:890px">
  <p class="quote">There were so many memorable moments you caught on the day from getting ready down to our guests reactions. One of the best moments we loved was how you captured our voices breaking during our vows showing our true emotions. The way you caught our natural emotions walking out to our confetti shoot was breath taking. The main part of the video that we adore is how you did the voice over of the reading and speeches.</p>
  <p class="quote" style="margin-top:26px">You guys were perfect! We honestly can't even remember seeing you guys shooting around us. You captured everything we wanted without taking us away from our day.</p>
  <p class="quote" style="margin-top:26px">One of our favourite things about our video was seeing moments that we missed on the day. Seeing our guests arrive, their reactions to speeches and during our drinks reception. You guys really did catch the joy of the day which you don't get as much just with photos.</p>
</div>

<!-- 04 -->
<div class="abs photo" style="left:0;top:3040px;width:660px;height:480px;background:linear-gradient(110deg,#2a2522,#6a5a50 40%,#c9c2b6 70%,#3a3632)" role="img" aria-label="Close-up of groom and bride about to kiss"></div>
<svg class="play" style="left:298px;top:3256px" viewBox="0 0 48 48"><circle cx="24" cy="24" r="22" fill="rgba(255,255,255,.75)"/><path d="M19 15l14 9-14 9z" fill="#555"/></svg>
<div class="abs avatar" style="left:738px;top:3128px;width:78px;height:78px" role="img" aria-label="Couple portrait"></div>
<div class="abs couple serif" style="left:830px;top:3143px">GRACE AND TOM</div>
<div class="abs venue" style="left:831px;top:3171px">Quayside Hotel, Newcastle</div>
<div class="abs quote-mark" style="left:820px;top:3194px">&ldquo;</div>
<p class="abs quote" style="left:712px;top:3238px;width:355px">Couldn't recommend Loren enough. Very professional and communication is great, responds very quick and keeps you updated on everything. The day was amazing and by the time we had finished breakfast the next day we had a short preview! Had all videos and stick within a week! Thank you again</p>
<div class="abs num" style="left:805px;top:3497px">04</div>
<div class="abs rule" style="left:845px;top:3516px;width:355px"></div>

<!-- 05 -->
<div class="abs photo" style="left:542px;top:3623px;width:658px;height:480px;background:linear-gradient(160deg,#3a2e20,#a8885a 35%,#e0cfa8 55%,#4a3a28 85%)" role="img" aria-label="Newlyweds celebrating under fairy lights as the bride raises her bouquet"></div>
<svg class="play" style="left:854px;top:3846px" viewBox="0 0 48 48"><circle cx="24" cy="24" r="22" fill="rgba(255,255,255,.75)"/><path d="M19 15l14 9-14 9z" fill="#555"/></svg>
<div class="abs avatar" style="left:185px;top:3732px;width:78px;height:78px" role="img" aria-label="Couple portrait"></div>
<div class="abs couple serif" style="left:278px;top:3746px">MEGAN AND LUKE</div>
<div class="abs venue" style="left:278px;top:3774px">Red Lion Stanhope</div>
<div class="abs quote-mark" style="left:262px;top:3798px">&ldquo;</div>
<p class="abs quote" style="left:135px;top:3838px;width:350px">One of the best decisions We made was choosing you guys to film our wedding! It's absolutely fantastic, it has everyone so emotional watching it, we can't thank you enough for capturing our special day! You were amazing from start to finish. Thanks so much.</p>
<div class="abs rule" style="left:0;top:4103px;width:345px"></div>
<div class="abs num" style="left:360px;top:4084px">05</div>

<div class="abs btn-more">LOAD MORE TESTIMONIALS</div>

<!-- Instagram -->
<div class="abs insta"></div>
<h2 class="abs insta-title serif">FOLLOW ME ON INSTAGRAM</h2>
<div class="abs tile" style="left:114px;background:linear-gradient(180deg,#b8b2a6,#6a6258)" role="img" aria-label="Couple walking down a village street"></div>
<div class="abs tile" style="left:279px;background:linear-gradient(180deg,#8a94a0,#3a4050)" role="img" aria-label="Groomsmen in tartan suits"></div>
<div class="abs tile" style="left:444px;background:linear-gradient(180deg,#e4e2dc,#9a9a88)" role="img" aria-label="Horse-drawn carriage in a field"></div>
<div class="abs tile" style="left:609px;background:linear-gradient(180deg,#6a6a6a,#2a2a2a)" role="img" aria-label="Wedding ceremony in black and white"></div>
<div class="abs tile" style="left:774px;background:linear-gradient(180deg,#7a7a7a,#1e1e1e)" role="img" aria-label="Bride laughing with guests"></div>
<div class="abs tile" style="left:939px;background:linear-gradient(180deg,#8fb0d8,#6a8a4a)" role="img" aria-label="Wedding party jumping on a lawn"></div>
<div class="abs follow">Follow me @lorenbriskfilms</div>

<!-- Footer -->
<div class="abs brand foot-brand" style="left:110px;top:4832px;width:190px">
  <div class="brand-mark" style="width:26px;height:26px"></div>
  <div class="brand-name" style="font-size:16px">LOREN BRISK</div>
  <div class="brand-sub">WEDDING FILMS</div>
</div>
<div class="abs social" style="left:154px"></div>
<div class="abs social" style="left:198px"></div>
<div class="abs social" style="left:242px"></div>

<div class="abs foot-head" style="left:412px;top:4868px">Contact</div>
<svg class="abs" style="left:412px;top:4919px" width="16" height="16" viewBox="0 0 16 16" fill="none" stroke="#999" stroke-width="1.2"><path d="M3 2h3l1 3-2 1a8 8 0 0 0 5 5l1-2 3 1v3a1 1 0 0 1-1 1A12 12 0 0 1 2 3a1 1 0 0 1 1-1z"/></svg>
<div class="abs foot-link" style="left:450px;top:4920px">07700 900 123</div>
<svg class="abs" style="left:412px;top:4965px" width="16" height="14" viewBox="0 0 16 14" fill="none" stroke="#999" stroke-width="1.2"><rect x="1" y="2" width="14" height="10"/><path d="M1 2l7 6 7-6"/></svg>
<div class="abs foot-link" style="left:450px;top:4964px">films@lorenbrisk.example</div>

<div class="abs foot-head" style="left:700px;top:4868px">Links</div>
<div class="abs foot-link" style="left:703px;top:4911px">FAQ's</div>
<div class="abs foot-link" style="left:703px;top:4946px">Wedding Photography</div>
<div class="abs foot-link" style="left:703px;top:4980px">Commercial</div>
<div class="abs foot-link" style="left:918px;top:4911px">North East Wedding Venues</div>
<div class="abs foot-link" style="left:918px;top:4946px">Free Speeches Guide</div>
<div class="abs foot-link" style="left:918px;top:4980px">Blog</div>

<div class="abs copy">© Copyright 2022 Loren Brisk Films Ltd All Rights Reserved</div>
</body>
</html>
```